Swift TECH Talentline by graduating students from college in two years

Based on the logo design, create stationary and business cards for
Dr. Velmor T Quenby, CEO, (555) 412-3076
and Lorna Pettigrew, Respresentative, (555) 238-6041
Address: 4197 Thistlemoor Lane, Quillmere Station, VA 24999
Incorporate elelments of the logo

Target Market(s)

USA

Font styles to use
Other font styles liked:
• match with the logo type style

```html
<!DOCTYPE html>
<html lang="en">
<head>
<meta charset="utf-8">
<title>Swift TECH Talentline — Stationery</title>
<link rel="stylesheet" href="https://fonts.googleapis.com/css2?family=Tinos:ital,wght@0,400;0,700;1,700&display=swap">
<style>
  :root {
    --backdrop: #d3d9dc;
    --paper: #ffffff;
    --gold: #f8c232;
    --gold-soft: #fbd56a;
    --navy: #1b2263;
    --ink: #1e2456;
    --ghost: #e6e6f3;
  }
  * { margin: 0; padding: 0; box-sizing: border-box; }
  html, body { width: 1200px; height: 916px; overflow: hidden; }
  body {
    position: relative;
    background: var(--backdrop);
    font-family: "Tinos", "Times New Roman", serif;
    color: var(--ink);
  }

  .sheet { position: absolute; background: var(--paper); overflow: hidden; box-shadow: 0 6px 14px rgba(40,50,60,.35); }

  /* business cards */
  .card { left: 68px; width: 438px; height: 250px; }
  .card--front { top: 66px; background: var(--gold); }
  .card--ceo { top: 339px; }
  .card--rep { top: 613px; }

  .pattern-gold {
    position: absolute; top: 0; right: 0; width: 124px; height: 76px;
    background: radial-gradient(ellipse at top right, var(--gold) 0%, rgba(248,194,50,.55) 45%, rgba(248,194,50,0) 78%);
  }
  .pattern-navy {
    position: absolute; bottom: 0; left: 0; width: 125px; height: 76px;
    background: radial-gradient(ellipse at bottom left, var(--navy) 0%, rgba(27,34,99,.55) 45%, rgba(27,34,99,0) 78%);
  }

  .brand-seal {
    position: absolute; border-radius: 50%;
    display: flex; align-items: center; justify-content: center; text-align: center;
    font-family: "Tinos", "Times New Roman", serif; font-weight: 700; color: var(--navy);
  }
  .card .brand-seal {
    left: 53px; top: 62px; width: 126px; height: 126px;
    border: 4px solid var(--gold); background: var(--paper);
    font-size: 15px; line-height: 1.15;
  }
  .card--front .brand-seal {
    left: 148px; top: 54px; width: 142px; height: 142px;
    border: 4px solid var(--navy); background: var(--paper);
    font-size: 17px;
  }

  .divider { position: absolute; left: 219px; top: 47px; width: 1.5px; height: 156px; background: var(--gold); }

  .card-details { position: absolute; left: 253px; top: 62px; }
  .person-name { font-weight: 700; font-size: 18.5px; color: var(--gold); line-height: 1; white-space: nowrap; }
  .person-role { font-size: 11.5px; margin-top: 3px; }
  .card-address { font-size: 11.5px; line-height: 15px; margin-top: 9px; white-space: nowrap; }
  .contact-list { list-style: none; margin-top: 9px; font-size: 11.5px; line-height: 15px; }
  .contact-list li { display: flex; align-items: center; gap: 6px; white-space: nowrap; }
  .icon { width: 10px; height: 10px; flex: none; }

  /* letterhead */
  .letterhead { left: 563px; top: 66px; width: 558px; height: 787px; }
  .letterhead .pattern-gold { width: 215px; height: 136px; }
  .letterhead .pattern-navy { width: 235px; height: 138px; }
  .letterhead .brand-seal {
    left: 31px; top: 24px; width: 66px; height: 66px;
    border: 3px solid var(--gold); background: var(--paper);
    font-size: 8.5px; line-height: 1.1;
  }
  .letterhead-mark {
    position: absolute; left: 103px; top: 222px; width: 348px; height: 348px;
    border-radius: 50%; border: 5px solid var(--ghost);
    display: flex; align-items: center; justify-content: center; text-align: center;
    font-weight: 700; font-size: 38px; line-height: 1.15; color: var(--ghost);
  }
  .letterhead-contact {
    position: absolute; right: 33px; top: 699px; list-style: none;
    font-size: 11.5px; line-height: 14.8px; text-align: right;
  }
  .letterhead-contact li { display: flex; justify-content: flex-end; align-items: center; gap: 7px; white-space: nowrap; }

  .caption {
    position: absolute; font-weight: 700; font-style: italic; color: #ffffff;
    text-shadow: 0 1px 3px rgba(60,70,80,.45); letter-spacing: 1px; white-space: nowrap;
  }
  .caption--cards { left: 145px; top: 870px; font-size: 32px; }
  .caption--letterhead { left: 728px; top: 862px; font-size: 33px; }
</style>
</head>
<body>

<svg width="0" height="0" style="position:absolute">
  <defs>
    <symbol id="i-phone" viewBox="0 0 10 10"><path d="M2 0.8 L3.6 2.8 L2.8 3.8 Q3.8 5.9 6.2 7.2 L7.2 6.4 L9.2 8 L8.2 9.4 Q3.6 9 0.6 2 Z" fill="none" stroke="#f8c232" stroke-width="1.1"/></symbol>
    <symbol id="i-globe" viewBox="0 0 10 10"><circle cx="5" cy="5" r="4.4" fill="#f8c232"/><path d="M0.6 5 H9.4 M5 0.6 V9.4" stroke="#fff" stroke-width="0.8"/></symbol>
    <symbol id="i-mail" viewBox="0 0 10 10"><rect x="0.6" y="2" width="8.8" height="6.4" fill="none" stroke="#f8c232" stroke-width="1.1"/><path d="M0.6 2 L5 5.6 L9.4 2" fill="none" stroke="#f8c232" stroke-width="1.1"/></symbol>
    <symbol id="i-pin" viewBox="0 0 10 10"><path d="M5 9.6 L1.8 5 A3.6 3.6 0 1 1 8.2 5 Z" fill="none" stroke="#f8c232" stroke-width="1.1"/><circle cx="5" cy="3.6" r="1.2" fill="#f8c232"/></symbol>
  </defs>
</svg>

<section class="sheet card card--front" aria-label="Business card front">
  <div class="brand-seal">Swift TECH<br>Talentline</div>
</section>

<section class="sheet card card--ceo" aria-label="Business card, CEO">
  <div class="pattern-gold" role="img" aria-label="Gold triangle mosaic fading from the corner"></div>
  <div class="pattern-navy" role="img" aria-label="Navy triangle mosaic fading from the corner"></div>
  <div class="brand-seal">Swift TECH<br>Talentline</div>
  <div class="divider"></div>
  <div class="card-details">
    <h2 class="person-name">Dr. Velmor T Quenby</h2>
    <p class="person-role">CEO</p>
    <p class="card-address">4197 Thistlemoor Lane,<br>Quillmere Station, VA 24999</p>
    <ul class="contact-list">
      <li><svg class="icon"><use href="#i-phone"/></svg>(555) 412-3076</li>
      <li><svg class="icon"><use href="#i-globe"/></svg>www.talentline-demo.com</li>
      <li><svg class="icon"><use href="#i-mail"/></svg>info@talentline-demo.com</li>
    </ul>
  </div>
</section>

<section class="sheet card card--rep" aria-label="Business card, Representative">
  <div class="pattern-gold" role="img" aria-label="Gold triangle mosaic fading from the corner"></div>
  <div class="pattern-navy" role="img" aria-label="Navy triangle mosaic fading from the corner"></div>
  <div class="brand-seal">Swift TECH<br>Talentline</div>
  <div class="divider"></div>
  <div class="card-details">
    <h2 class="person-name">Lorna Pettigrew</h2>
    <p class="person-role">Respresentative</p>
    <p class="card-address">4197 Thistlemoor Lane,<br>Quillmere Station, VA 24999</p>
    <ul class="contact-list">
      <li><svg class="icon"><use href="#i-phone"/></svg>(555) 238-6041</li>
      <li><svg class="icon"><use href="#i-globe"/></svg>www.talentline-demo.com</li>
      <li><svg class="icon"><use href="#i-mail"/></svg>info@talentline-demo.com</li>
    </ul>
  </div>
</section>

<section class="sheet letterhead" aria-label="A4 letterhead">
  <div class="pattern-gold" role="img" aria-label="Gold triangle mosaic fading from the corner"></div>
  <div class="pattern-navy" role="img" aria-label="Navy triangle mosaic fading from the corner"></div>
  <div class="brand-seal">Swift TECH<br>Talentline</div>
  <div class="letterhead-mark">Swift TECH<br>Talentline</div>
  <ul class="letterhead-contact">
    <li>(555) 238-6041<svg class="icon"><use href="#i-phone"/></svg></li>
    <li>www.talentline-demo.com<svg class="icon"><use href="#i-globe"/></svg></li>
    <li>info@talentline-demo.com<svg class="icon"><use href="#i-mail"/></svg></li>
    <li>4197 Thistlemoor Lane, Quillmere Station, VA 24999<svg class="icon"><use href="#i-pin"/></svg></li>
  </ul>
</section>

<p class="caption caption--cards">Business card</p>
<p class="caption caption--letterhead">A4 Letterhead</p>

</body>
</html>
```